Social Media Cover and Profile

We already have our own logo. We just need a fresh design on our social media pages. We are not happy with our current designs. We would like to incorporate our YIKE billboard and the colors are blue (#05143f) and white. You can also incorporate silver as well. We are a family law office (Divorce and Custody) We no longer want to incorporate the Spire of Dunvale photo that we are currently using. You can look at our Facebook page; The Law Office of Miles T. Hadley.

Target Market(s)

Potential Clients

Industry/Entity Type

Family Law

Logo Text

Our Logo Is The Law Office of Miles T. Hadley with the Sheild

Requirements
Must have
• Text to include:
Central Pennslyvania's Premier Family Law Firm

Ability to be resized to and used as all images in social media, including but not limited to: Youtube Channel art, Facebook Cover and Profile.
Nice to have
• Darker color but we are open to "bright" ideas.

```html
<!DOCTYPE html>
<html lang="en">
<head>
<meta charset="utf-8">
<title>Miles T. Hadley – Social Cover and Profile</title>
<link href="https://fonts.googleapis.com/css2?family=Cinzel:wght@400;500;600&family=Archivo+Black&display=swap" rel="stylesheet">
<style>
  :root{
    --navy:#05143f;
    --white:#ffffff;
    --page:#e9ebee;
    --cover-light:#ffffff;
    --cover-shade:#e6e7ea;
    --silver-hi:#f4f4f4;
    --silver-mid:#b9babd;
    --silver-lo:#7d7f83;
    --ink-soft:#3a3d44;
  }
  *{margin:0;padding:0;box-sizing:border-box}
  html,body{width:1200px;height:643px;overflow:hidden;background:var(--page)}
  body{position:relative;font-family:"Cinzel",serif}

  .cover{
    position:absolute;left:30px;top:24px;width:1140px;height:434px;
    background:radial-gradient(ellipse at 55% 40%,var(--cover-light) 0%,#f6f6f7 45%,var(--cover-shade) 100%);
    box-shadow:0 1px 3px rgba(0,0,0,.12);
    overflow:hidden;
  }
  .brand{position:absolute;left:36px;top:28px;display:flex;align-items:center;gap:16px;color:var(--navy)}
  .brand-mark{width:70px;height:70px;border-radius:50%;background:var(--navy)}
  .brand-name{display:flex;flex-direction:column;line-height:1}
  .brand-name .small,.brand-name .large{font-family:"Cinzel",serif;font-weight:500;color:var(--navy)}
  .brand-name .small{font-size:14px;letter-spacing:.5px;margin-bottom:4px}
  .brand-name .large{font-size:32px;letter-spacing:.5px}

  .headline{
    position:absolute;left:0;right:0;top:110px;text-align:center;
    font-family:"Archivo Black",sans-serif;font-size:205px;line-height:1;letter-spacing:14px;
    background:linear-gradient(180deg,var(--silver-hi) 0%,var(--silver-mid) 45%,var(--silver-lo) 70%,#d9dadc 100%);
    -webkit-background-clip:text;background-clip:text;color:transparent;
    filter:drop-shadow(0 6px 6px rgba(0,0,0,.18));
  }
  .tagline{
    position:absolute;left:0;right:0;top:334px;text-align:center;
    font-size:21px;letter-spacing:3px;color:var(--ink-soft);font-weight:400;
  }
  .web{
    position:absolute;right:40px;top:378px;font-size:27px;font-weight:500;
    color:var(--navy);border-bottom:1.5px solid var(--navy);line-height:1.15;
  }

  .profile{
    position:absolute;left:30px;top:474px;width:160px;height:160px;border-radius:50%;
    background:var(--white);box-shadow:0 0 0 4px var(--white),0 1px 4px rgba(0,0,0,.2);
    display:flex;align-items:center;justify-content:center;gap:6px;
  }
  .profile .brand-mark{width:26px;height:26px}
  .profile .brand-name .small{font-size:6px;margin-bottom:2px}
  .profile .brand-name .large{font-size:12px}
</style>
</head>
<body>
  <section class="cover">
    <div class="brand">
      <div class="brand-mark"></div>
      <div class="brand-name">
        <span class="small">THE LAW OFFICE OF</span>
        <span class="large">MILES T HADLEY</span>
      </div>
    </div>
    <div class="headline">YIKE</div>
    <div class="tagline">CENTRAL PENNSLYVANIA'S PREMIER FAMILY LAW FIRM</div>
    <div class="web">MILESHADLEYLAW.COM</div>
  </section>

  <section class="profile">
    <div class="brand-mark"></div>
    <div class="brand-name">
      <span class="small">THE LAW OFFICE OF</span>
      <span class="large">MILES T HADLEY</span>
    </div>
  </section>
</body>
</html>
```